Design business cards for Ironvale Barbers (Opening March so won't need finalised till January2018

Ironvale Barbers is the new age barbers and skincare for all men. Creating tailor made haircuts & customised skincare solutions for the perfect healthy manly look. The Barbers will have a industrial, rustic, worldly feel about it. Rustic red brick wall with old wine barrels as the work stations with the old fashion barber chairs. Concrete floor and a bit corrugated iron around.
Target Market(s)
Professional males who like a great haircut, wet shave and may consider a facial if in the right environment. Total pampering experience in a boys environment.
Industry/Entity Type
Barber
Contact Information for Business Card
Front- Logo - address is 42 Kowhai Rd Taupo
Ph - (07) 548 9163
www.ironvalebarbers.com
email - hello@ironvale.co.nz
Back of card
Mens Haircare - Wet Shaving - Facials - Skin Prescriptions
We are doing a loyalty program - 6 squares numbered then 7th free
Colors
Designer to choose colors to be used in the design.
Requirements
Must have
- Clean simple easy to read.
Nice to have
- Our current colours are white font on black background but thinking we need to introduce another colour. Maybe white logo on a copper, bronze or rusty background. Or even a rustic red brick wall with white writing. Want it clean simple to read. Maybe a burgundy?
Should not have
- no images like heads, scissors, razors please

```html
<!DOCTYPE html>
<html lang="en">
<head>
<meta charset="utf-8">
<title>Ironvale Barbers — Business Cards</title>
<link rel="stylesheet" href="https://fonts.googleapis.com/css2?family=Roboto+Condensed:wght@400;700&display=swap">
<style>
  :root {
    --canvas-bg: #e5e5e5;
    --card-shadow: #bdbdbd;
    --rust: #a0614f;
    --white: #ffffff;
    --ink: #000000;
    --rule: #333333;
  }
  * { box-sizing: border-box; margin: 0; padding: 0; }
  html, body {
    width: 1200px; height: 1000px; overflow: hidden;
    background: var(--canvas-bg);
    font-family: "Roboto Condensed", "Arial Narrow", sans-serif;
  }
  .canvas { position: relative; width: 1200px; height: 1000px; }
  .card {
    position: absolute; left: 280px; width: 640px; height: 392px;
    box-shadow: 7px 7px 0 var(--card-shadow);
  }
  .card--front { top: 78px; background: var(--rust); color: var(--white); }
  .card--back  { top: 530px; background: var(--white); color: var(--ink); }
  .card__frame { position: absolute; inset: 0; width: 640px; height: 392px; }
  .wordmark {
    position: absolute; left: 0; right: 0; text-align: center;
    font-weight: 700; text-transform: uppercase; line-height: 1;
  }
  .card--front .wordmark { top: 84px; font-size: 64px; letter-spacing: 1px; }
  .card--front .wordmark__sub { display: block; font-size: 26px; letter-spacing: 8px; margin-top: 6px; }
  .card--back .wordmark { top: 60px; font-size: 34px; }
  .card--back .wordmark__sub { display: block; font-size: 14px; letter-spacing: 4px; margin-top: 3px; }
  .contact {
    position: absolute; top: 229px; left: 0; right: 0;
    text-align: center; font-size: 21px; line-height: 28px; font-weight: 400;
  }
  .services {
    position: absolute; top: 142px; left: 0; right: 0;
    text-align: center; font-weight: 700; font-size: 21px; line-height: 27px;
    text-transform: uppercase;
  }
  .services__sep { display: inline-block; width: 1.5px; height: 16px; background: var(--ink); margin: 0 12px; vertical-align: -1px; }
  .appointment {
    position: absolute; left: 133px; top: 226px; width: 374px;
    border-collapse: collapse; font-size: 21px;
  }
  .appointment td { border: 1px solid var(--rule); height: 52px; padding: 0 18px; }
  .appointment .appointment__label { width: 126px; }
</style>
</head>
<body>
<main class="canvas">
  <section class="card card--front" aria-label="Card front">
    <svg class="card__frame" viewBox="0 0 640 392" aria-hidden="true">
      <path d="M41 23 H599 A18 18 0 0 0 617 41 V351 A18 18 0 0 0 599 369 H41 A18 18 0 0 0 23 351 V41 A18 18 0 0 0 41 23 Z" fill="none" stroke="#fff" stroke-width="3"/>
      <path d="M42 30 H598 A12 12 0 0 0 610 42 V350 A12 12 0 0 0 598 362 H42 A12 12 0 0 0 30 350 V42 A12 12 0 0 0 42 30 Z" fill="none" stroke="#fff" stroke-width="1.5"/>
    </svg>
    <h1 class="wordmark">Ironvale<span class="wordmark__sub">Barbers</span></h1>
    <p class="contact">00-000 0000<br>ironvalebarbers.com<br>hello@ironvale.co.nz</p>
  </section>

  <section class="card card--back" aria-label="Card back">
    <svg class="card__frame" viewBox="0 0 640 392" aria-hidden="true">
      <path d="M45 25 H595 A20 20 0 0 0 615 45 V347 A20 20 0 0 0 595 367 H45 A20 20 0 0 0 25 347 V45 A20 20 0 0 0 45 25 Z" fill="none" stroke="#000" stroke-width="5"/>
      <path d="M44 32 H596 A12 12 0 0 0 608 44 V348 A12 12 0 0 0 596 360 H44 A12 12 0 0 0 32 348 V44 A12 12 0 0 0 44 32 Z" fill="none" stroke="#000" stroke-width="1.5"/>
    </svg>
    <h2 class="wordmark">Ironvale<span class="wordmark__sub">Barbers</span></h2>
    <p class="services">Mens Haircare<span class="services__sep"></span>Wet Shaving<br>Facials<span class="services__sep"></span>Skin Prescriptions</p>
    <table class="appointment">
      <tr><td class="appointment__label">Date</td><td></td></tr>
      <tr><td class="appointment__label">Time</td><td></td></tr>
    </table>
  </section>
</main>
</body>
</html>
```